Design for Employee Baseball Cards

Looking to design baseball cards for my employees. Trying to replicate famous baseball card design with swapping in an employee and listing there stats and fun facts. These cards will be inserted into boxes so customers can receive with their orders. Cards allow customers to put a face to the name they've always corresponded with, which makes their experience personable and more memorable.

Looking for a front and back design template. We are open to the design, but would like it to resemble a baseball/playing card.
Size: 2.5" x 3.5" vertical
Here is our website which can be referenced for color pallet and tone.
https://www.crateswithmarlow.com/

Attached is an example of a vintage baseball. Can we see some versions like this?

Front
- Person's name
- Title/Department
- Crates With Marlow logo
- Person's photo - this will be an action shot like a baseball card

Back
I'm open to the design and content of the back. We want it to resemble a back of a baseball card as best as possible. Normally, baseball cards will have stats by year. Instead, we can have stats and fun facts like the following

Items for Back
- Bio
- Year started at CWM
- Department
- Years of experience
- Specialty
- Secret skill
- What you love about CWM
- Favorite quote
- Fun fact
- Passion outside of CWM
- Person's photo - we can include a smaller headshot

Font styles to use
Sans Serif

Colors
0054AA
0677BA
7BADD7
CADEEF
E8F1F8

Requirements
Must have
• The deliverable must be a template PSD or AI that we can swap in photos and edit text for each person's card.

```html
<!DOCTYPE html>
<html lang="en">
<head>
<meta charset="utf-8">
<title>Crates With Marlow – Employee Card Front and Back</title>
<link rel="stylesheet" href="https://fonts.googleapis.com/css2?family=Montserrat:wght@400;500;600;700;800&family=Oswald:wght@500&family=Archivo+Black&family=Short+Stack&display=swap">
<style>
  :root {
    --ink: #0f2a33;
    --rust: #cf4a35;
    --gold: #d69a3c;
    --cream: #f6e3d4;
    --cream-deep: #ecd1bd;
    --photo-light: #f3dccb;
    --photo-deep: #e6c2aa;
    --headshot: #d9d4d0;
    --white: #ffffff;
    --brand-blue: #1f3f7a;
    --backdrop: #c9c9c9;
  }
  * { margin: 0; padding: 0; box-sizing: border-box; }
  html, body { width: 1200px; height: 865px; overflow: hidden; }
  body {
    background: var(--backdrop);
    font-family: "Montserrat", sans-serif;
    position: relative;
  }
  .card {
    position: absolute;
    top: 125px;
    width: 440px;
    height: 616px;
  }
  .card--front { left: 120px; }
  .card--back { left: 640px; }
  .card__art { position: absolute; inset: 0; width: 440px; height: 616px; }

  .brand-mark { width: 12px; height: 12px; border-radius: 50%; background: var(--brand-blue); flex: none; }
  .brand-name { font-weight: 600; color: var(--brand-blue); white-space: nowrap; }

  /* Front */
  .front-brand {
    position: absolute; left: 160px; top: 70px; width: 120px; height: 110px;
    display: flex; align-items: center; justify-content: center; gap: 6px;
  }
  .front-brand .brand-name { font-size: 13px; line-height: 1.15; }
  .player-name {
    position: absolute; left: 0; right: 0; top: 538px;
    text-align: center; font-size: 22px; color: var(--gold); letter-spacing: .5px; white-space: nowrap;
  }
  .player-name__first { font-weight: 500; }
  .player-name__last { font-weight: 800; }
  .player-role {
    position: absolute; left: 0; right: 0; top: 570px;
    display: flex; align-items: center; justify-content: center; gap: 10px;
    color: var(--white); font-weight: 700; font-size: 15px; white-space: nowrap;
  }
  .player-role::before, .player-role::after {
    content: ""; height: 1.5px; width: 110px; background: var(--white); opacity: .85;
  }

  /* Back */
  .back-name {
    position: absolute; left: 0; right: 0; top: 190px; text-align: center;
    font-family: "Archivo Black", sans-serif; font-size: 24px; line-height: 1.1; color: var(--ink); letter-spacing: 1px;
  }
  .back-title {
    position: absolute; left: 0; right: 0; top: 220px; text-align: center;
    font-weight: 700; font-size: 14px; color: var(--rust); letter-spacing: .5px;
  }
  .stats {
    position: absolute; left: 56px; top: 248px; width: 160px;
    font-family: "Oswald", sans-serif; font-size: 10.5px; line-height: 1.8; color: var(--ink); white-space: nowrap;
  }
  .stats span + span { margin-left: 6px; }
  .trivia {
    position: absolute; left: 226px; top: 254px; width: 78px; text-align: center;
    font-family: "Oswald", sans-serif; font-size: 10.5px; line-height: 1.6; color: var(--ink);
  }
  .tagline {
    position: absolute; left: 44px; right: 44px; top: 322px; text-align: center;
    font-family: "Short Stack", sans-serif; font-size: 15px; line-height: 1.3; color: var(--cream);
  }
  .record { position: absolute; left: 56px; top: 380px; width: 328px; color: var(--ink); }
  .record__title {
    background: var(--ink); color: var(--cream); border-radius: 10px 10px 0 0;
    text-align: center; font-weight: 700; font-size: 10.5px; letter-spacing: 3px; padding: 4px 0 3px;
  }
  .record__table {
    width: 100%; border-collapse: collapse; font-size: 8.5px; font-weight: 500;
    background: var(--cream-deep); border: 1.5px solid var(--ink); border-top: none;
  }
  .record__table th { font-weight: 700; padding: 3px 6px 2px; border-bottom: 1px solid var(--ink); text-align: left; }
  .record__table td { padding: 1.5px 6px; line-height: 1.2; }
  .record__table .wins { text-align: center; }
  .record__table .losses { text-align: center; width: 60px; }
  .printed { position: absolute; right: 60px; top: 530px; font-size: 6px; font-weight: 700; color: var(--ink); }
  .back-brand {
    position: absolute; left: 0; right: 0; top: 552px;
    display: flex; justify-content: center; align-items: center; gap: 8px;
  }
  .back-brand .brand-name { font-size: 15px; }
  .back-brand .brand-mark { width: 14px; height: 14px; }
</style>
</head>
<body>

<section class="card card--front" aria-label="Employee card front">
  <svg class="card__art" viewBox="0 0 440 616">
    <defs>
      <linearGradient id="photoTone" x1="0" y1="0" x2="0" y2="1">
        <stop offset="0" stop-color="var(--photo-light)"/><stop offset="1" stop-color="var(--photo-deep)"/>
      </linearGradient>
    </defs>
    <rect width="440" height="616" rx="18" fill="var(--ink)"/>
    <polygon points="250,110 440,90 440,250 340,250" fill="var(--rust)"/>
    <polygon points="0,200 150,178 120,330 0,330" fill="var(--rust)"/>
    <g fill="var(--gold)">
      <rect x="18" y="350" width="28" height="38"/><rect x="18" y="416" width="28" height="30"/>
      <rect x="18" y="490" width="28" height="24"/><rect x="394" y="200" width="28" height="36"/>
      <rect x="394" y="268" width="28" height="30"/><rect x="394" y="456" width="28" height="26"/>
    </g>
    <g fill="var(--rust)">
      <rect x="18" y="460" width="28" height="18"/><rect x="394" y="380" width="28" height="40"/>
    </g>
    <g fill="var(--gold)" font-size="13">
      <text x="52" y="98">✦✦✦✦</text><text x="318" y="76">✦✦✦✦</text>
    </g>
    <path d="M50,228 Q50,196 82,188 Q132,178 162,156 L278,156 Q308,178 358,188 Q390,196 390,228 L390,522 Q220,494 50,522 Z" fill="var(--cream)"/>
    <path d="M64,234 Q64,208 90,202 Q138,192 168,170 L272,170 Q302,192 350,202 Q376,208 376,234 L376,506 Q220,480 64,506 Z" fill="none" stroke="var(--gold)" stroke-width="2"/>
    <path role="img" aria-label="Action photo of the employee posing with a baseball bat" d="M78,240 Q78,218 98,214 Q142,204 172,184 L268,184 Q298,204 342,214 Q362,218 362,240 L362,494 Q220,470 78,494 Z" fill="url(#photoTone)"/>
    <circle cx="220" cy="125" r="66" fill="var(--ink)"/>
    <circle cx="220" cy="125" r="56" fill="var(--white)" stroke="var(--gold)" stroke-width="2"/>
    <line x1="30" y1="598" x2="410" y2="598" stroke="var(--white)" stroke-width="1" opacity=".6"/>
  </svg>
  <div class="front-brand">
    <span class="brand-mark"></span>
    <span class="brand-name">Crates<br>With Marlow</span>
  </div>
  <p class="player-name"><span class="player-name__first">DARREN K. </span><span class="player-name__last">HOLLOWAY</span></p>
  <p class="player-role">Job Position</p>
</section>

<section class="card card--back" aria-label="Employee card back">
  <svg class="card__art" viewBox="0 0 440 616">
    <rect width="440" height="616" rx="18" fill="var(--ink)"/>
    <polygon points="0,165 170,150 120,290 0,290" fill="var(--rust)"/>
    <polygon points="290,185 440,200 440,320 350,310" fill="var(--rust)"/>
    <g fill="var(--gold)">
      <rect x="12" y="310" width="24" height="34"/><rect x="12" y="392" width="24" height="26"/>
      <rect x="12" y="450" width="24" height="34"/><rect x="404" y="336" width="24" height="30"/>
      <rect x="404" y="416" width="24" height="34"/><rect x="404" y="506" width="24" height="28"/>
    </g>
    <g fill="var(--rust)">
      <rect x="12" y="360" width="24" height="20"/><rect x="404" y="466" width="24" height="24"/>
    </g>
    <g fill="var(--gold)" font-size="13">
      <text x="62" y="62">✦✦✦✦</text><text x="318" y="94">✦✦✦✦</text>
    </g>
    <path d="M40,208 Q40,180 70,174 Q122,166 160,140 L280,140 Q318,166 370,174 Q400,180 400,208 L400,540 Q372,550 352,570 Q322,600 282,600 L158,600 Q118,600 88,570 Q68,550 40,540 Z" fill="var(--cream)"/>
    <path d="M52,214 Q52,192 76,187 Q126,178 164,154 L276,154 Q314,178 364,187 Q388,192 388,214 L388,530" fill="none" stroke="var(--gold)" stroke-width="1.8"/>
    <line x1="220" y1="252" x2="218" y2="306" stroke="var(--rust)" stroke-width="1.5"/>
    <line x1="310" y1="252" x2="308" y2="306" stroke="var(--rust)" stroke-width="1.5"/>
    <circle role="img" aria-label="Small drawn batter emblem" cx="350" cy="280" r="20" fill="var(--cream-deep)" stroke="var(--ink)" stroke-width="2"/>
    <rect x="40" y="314" width="360" height="60" fill="var(--gold)"/>
    <circle cx="220" cy="112" r="62" fill="var(--ink)"/>
    <circle role="img" aria-label="Headshot of the employee holding a bat" cx="220" cy="112" r="54" fill="var(--headshot)" stroke="var(--rust)" stroke-width="2.5"/>
  </svg>
  <p class="back-name">TOM KESSLER</p>
  <p class="back-title">SALESMAN</p>
  <div class="stats">
    <p><span>HT: 5'6"</span><span>WT: 130</span><span>BORN: 6-30-35</span></p>
    <p>WRITES: RIGHT</p>
    <p>HOME: SOMEWHERE IN NEW JERSEY</p>
  </div>
  <p class="trivia">WHEN WAS<br>HIS FIRST SALE<br>MADE?</p>
  <p class="tagline">World's Greatest Salesman<br>(in his own mind)</p>
  <div class="record">
    <p class="record__title">CRATES WITH MARLOW RECORD</p>
    <table class="record__table">
      <thead><tr><th>YEAR</th><th class="wins">WINS</th><th class="losses">LOSSES</th></tr></thead>
      <tbody>
        <tr><td>2021</td><td class="wins">NOT TOO DAMN BAD</td><td class="losses">0</td></tr>
        <tr><td>2020</td><td class="wins">GETTIN' BETTER</td><td class="losses">0</td></tr>
        <tr><td>2019</td><td class="wins">ON THE UPSWING</td><td class="losses">0</td></tr>
        <tr><td>2018</td><td class="wins">IMPROVING</td><td class="losses">0</td></tr>
        <tr><td>2017</td><td class="wins">FUTURE'S LOOKING BRIGHT</td><td class="losses">0</td></tr>
        <tr><td>2016</td><td class="wins">HOLDING HIS OWN</td><td class="losses">0</td></tr>
        <tr><td>2015</td><td class="wins">A FEW</td><td class="losses">0</td></tr>
        <tr><td>2014</td><td class="wins">LUCKY TO HAVE A JOB</td><td class="losses">0</td></tr>
      </tbody>
    </table>
  </div>
  <p class="printed">PRTD. IN U.S.A.</p>
  <div class="back-brand">
    <span class="brand-mark"></span>
    <span class="brand-name">Crates With Marlow</span>
  </div>
</section>

</body>
</html>
```